Zielgruppe
Steuerberater, Zielgruppe: Mandanten
Aufgabenstellung
Es sollten keine Balken an den Rändern vorhanden sein, so dass das Briefpapier mit dem eigenen Farbdrucker bedruckt werden kann.
-Keine Balken an den Rändern
-Wir wollen kein Briefpapier bedrucken lassen, soll mit dem eigenen Drucker bedruckbar sein
Die Schriftart CG Omega sollte installiert sein, für die korrekte Darstellung.

```html
<!DOCTYPE html>
<html lang="de">
<head>
<meta charset="utf-8">
<title>Briefbogen Kanzlei Valdren</title>
<link href="https://fonts.googleapis.com/css2?family=Lato:wght@400;700&display=swap" rel="stylesheet">
<style>
  :root {
    --navy: #1b2a57;
    --ink: #3a3d40;
    --paper: #ffffff;
  }
  html, body {
    margin: 0;
    padding: 0;
    overflow: hidden;
  }
  body {
    width: 848px;
    height: 1200px;
    background: var(--paper);
    font-family: "Lato", sans-serif;
    color: var(--ink);
  }
  .letterhead {
    position: relative;
    width: 848px;
    height: 1200px;
  }
  .brand {
    position: absolute;
    left: 550px;
    top: 66px;
    font-size: 26px;
    font-weight: 400;
    color: var(--navy);
    line-height: 1;
    white-space: nowrap;
  }
  .sender-line {
    position: absolute;
    left: 106px;
    top: 192px;
    font-size: 11px;
    white-space: nowrap;
  }
  .sender-line strong {
    color: var(--navy);
    font-weight: 700;
  }
  .sender-line .sep {
    margin: 0 6px;
  }
  .contact {
    position: absolute;
    left: 673px;
    top: 190px;
    font-size: 12px;
    line-height: 18.5px;
  }
  .contact p {
    margin: 0;
  }
  .contact .person {
    margin-bottom: 10px;
  }
  .contact .person-name {
    color: var(--navy);
    font-weight: 700;
  }
  .contact .address {
    margin-top: 19px;
    margin-bottom: 12px;
  }
  .contact .phone {
    margin-bottom: 12px;
  }
  .contact .label {
    display: inline-block;
    width: 53px;
  }
  .footer {
    position: absolute;
    left: 28px;
    top: 1176px;
    font-size: 11px;
    white-space: nowrap;
  }
  .footer strong {
    font-weight: 700;
  }
  .footer .gap {
    margin-left: 8px;
  }
</style>
</head>
<body>
<main class="letterhead">
  <header class="brand">Kanzlei Valdren</header>

  <div class="sender-line">
    <strong>Kanzlei Valdren</strong><span class="sep">I</span>Lindenweg 14<span class="sep">I</span>71099 Falkental
  </div>

  <aside class="contact">
    <div class="person">
      <p class="person-name">Tarek Valdren</p>
      <p>Diplom-Kaufmann</p>
      <p>Steuerberater</p>
    </div>
    <div class="person">
      <p class="person-name">Aron Valdren</p>
      <p>Rechtsanwalt</p>
      <p>Fachanwalt für Steuerrecht</p>
    </div>
    <div class="address">
      <p>Lindenweg 14</p>
      <p>71099 Falkental</p>
    </div>
    <div class="phone">
      <p><span class="label">Telefon:</span>07031 – 554210</p>
      <p><span class="label">Telefax:</span>07031 – 554211</p>
    </div>
    <div class="web">
      <p>mail@kanzlei-valdren.de</p>
      <p>www.kanzlei-valdren.de</p>
    </div>
  </aside>

  <footer class="footer">
    <strong>Bankverbindung</strong> I Kanzlei Valdren GbR • Nordstadt Bank AG • IBAN: DE12 3456 0000 0987 6543 21 • BIC: NRDBDEFFXXX<span class="gap"></span> <strong>Umsatzsteuer-ID</strong> I DE123456789
  </footer>
</main>
</body>
</html>
```